Verostel business card

Business card for sustainable investment company called "Verostel". Verostel is an exchange platform selling carbon credits between buyers and sellers. Carbon Credits are an environmental commodity for reducing global carbon emissions.

the card should obviously have our logo and the theme should be sustainability/environment mixed with a trading platform.

Contact Information for Business Card

Logo, Name, Title, Phone, Email

Colors
0054AA
0677BA
7BADD7
CADEEF
E8F1F8
0094D4
00A9DD
6FCCEA
C7EBF8
E9F6FB
00AB8E
00BBA5
67D7C9
C6EFE9
E9F9F6
59FF00
82FF00
B8FF75
E3FFCB
F4FFEA

```html
<!DOCTYPE html>
<html lang="en">
<head>
<meta charset="utf-8">
<title>Verostel business card</title>
<link rel="stylesheet" href="https://fonts.googleapis.com/css2?family=Montserrat:wght@400;500;700&display=swap">
<style>
  :root {
    --stage: #3b3b3d;
    --kraft: #d6b077;
    --kraft-shade: #cfa86e;
    --navy: #112a55;
    --ink: #1b1b1b;
    --accent: #4a8fd6;
    --accent-light: #6fcce8;
  }
  * { box-sizing: border-box; margin: 0; padding: 0; }
  html, body { width: 1200px; height: 1000px; overflow: hidden; }
  body {
    background: var(--stage);
    font-family: "Montserrat", Arial, sans-serif;
    position: relative;
  }
  .card {
    position: absolute;
    left: 240px;
    width: 720px;
    height: 411px;
    background: radial-gradient(circle at 30% 30%, var(--kraft) 0%, var(--kraft-shade) 100%);
    box-shadow: 0 14px 30px rgba(0,0,0,0.45);
  }
  .card--front { top: 60px; }
  .card--back { top: 530px; }

  .brand {
    display: flex;
    align-items: center;
    gap: 18px;
    color: var(--navy);
    font-weight: 700;
    letter-spacing: 0.02em;
  }
  .brand__dot {
    border-radius: 50%;
    background: var(--accent);
    flex: none;
  }
  .card--front .brand {
    position: absolute;
    left: 50%; top: 50%;
    transform: translate(-50%, -50%);
    font-size: 62px;
  }
  .card--front .brand__dot { width: 70px; height: 70px; }

  .card--back .brand {
    position: absolute;
    left: 44px; top: 140px;
    font-size: 34px;
    gap: 12px;
  }
  .card--back .brand__dot { width: 42px; height: 42px; }

  .divider {
    position: absolute;
    left: 372px; top: 95px;
    width: 2px; height: 230px;
    background: var(--accent);
  }
  .contact {
    position: absolute;
    left: 400px; top: 100px;
    color: var(--ink);
  }
  .contact__name {
    font-size: 26px;
    font-weight: 700;
    color: var(--navy);
    letter-spacing: 0.06em;
    line-height: 1;
  }
  .contact__title {
    font-size: 15px;
    font-weight: 500;
    letter-spacing: 0.06em;
    margin-top: 4px;
  }
  .contact__address {
    font-size: 14.5px;
    line-height: 1.4;
    margin-top: 18px;
    width: 290px;
  }
  .contact__list {
    list-style: none;
    margin-top: 14px;
    font-size: 15px;
    line-height: 1.75;
  }
  .contact__list li { display: flex; align-items: center; gap: 10px; }
  .contact__list svg { width: 14px; height: 14px; fill: var(--accent); flex: none; }
</style>
</head>
<body>
  <section class="card card--front">
    <div class="brand"><span class="brand__dot"></span>VEROSTEL</div>
  </section>

  <section class="card card--back">
    <div class="brand"><span class="brand__dot"></span>VEROSTEL</div>
    <div class="divider"></div>
    <div class="contact">
      <p class="contact__name">ARLEN VOSS</p>
      <p class="contact__title">MANAGER</p>
      <p class="contact__address">2217 Harbor Crest Rd. Linden Park Ave Fairmont, OR 97402</p>
      <ul class="contact__list">
        <li>
          <svg viewBox="0 0 24 24"><path d="M6.6 10.8a15.1 15.1 0 0 0 6.6 6.6l2.2-2.2a1 1 0 0 1 1-.25 11.4 11.4 0 0 0 3.6.57 1 1 0 0 1 1 1V20a1 1 0 0 1-1 1A17 17 0 0 1 3 4a1 1 0 0 1 1-1h3.5a1 1 0 0 1 1 1c0 1.25.2 2.45.57 3.6a1 1 0 0 1-.25 1z"/></svg>
          123-456-7890
        </li>
        <li>
          <svg viewBox="0 0 24 24"><path d="M2 5h20v14H2z M2 5l10 8 10-8" /></svg>
          info@youremail.com
        </li>
        <li>
          <svg viewBox="0 0 24 24"><path d="M12 2a10 10 0 1 0 0 20 10 10 0 0 0 0-20zm6.9 6h-2.9a15.7 15.7 0 0 0-1.4-3.6A8 8 0 0 1 18.9 8zM12 4c.8 1.2 1.5 2.5 1.9 4h-3.8c.4-1.5 1.1-2.8 1.9-4zM4.3 14a8 8 0 0 1 0-4h3.4a16 16 0 0 0 0 4zm.8 2h2.9c.3 1.3.8 2.5 1.4 3.6A8 8 0 0 1 5.1 16zM8 8H5.1a8 8 0 0 1 4.3-3.6C8.8 5.5 8.3 6.7 8 8zm4 12c-.8-1.2-1.5-2.5-1.9-4h3.8c-.4 1.5-1.1 2.8-1.9 4zm2.3-6H9.7a14.7 14.7 0 0 1 0-4h4.6a14.7 14.7 0 0 1 0 4zm.3 5.6c.6-1.1 1.1-2.3 1.4-3.6h2.9a8 8 0 0 1-4.3 3.6zM16.3 14a16 16 0 0 0 0-4h3.4a8 8 0 0 1 0 4z"/></svg>
          www.yourwebsite.com
        </li>
      </ul>
    </div>
  </section>
</body>
</html>
```